R & T Summit Construction Business Card ideas

We want a business card to represents our company in a way that looks professional but is also a business card that is unique!

Industry/Entity Type

Construction Company

Contact Information for Business Card

open to all design ideas, just want to be able to see different options to choose from in either color or grayscale.

Requirements
Must have
• Our names and phone numbers
• Nolan Pritchett 512-804-2271
• Curtis Hale 512-693-1804
• Business logo

```html
<!DOCTYPE html>
<html lang="en">
<head>
<meta charset="utf-8">
<title>R &amp; T Summit Construction – Business Cards</title>
<link href="https://fonts.googleapis.com/css2?family=Tinos&family=Montserrat:wght@500&display=swap" rel="stylesheet">
<style>
  :root {
    --bg: #efefef;
    --card-light: #ffffff;
    --card-dark: #070707;
    --ink: #111111;
    --ink-inverse: #ffffff;
    --shadow: 0 2px 6px rgba(0,0,0,0.12);
  }
  * { margin: 0; padding: 0; box-sizing: border-box; }
  html, body { width: 1200px; height: 1000px; overflow: hidden; }
  body {
    background: radial-gradient(ellipse at 50% 35%, #fafafa 0%, var(--bg) 100%);
    position: relative;
    font-family: "Tinos", "Times New Roman", serif;
  }
  .card {
    position: absolute;
    width: 479px;
    height: 273px;
    border-radius: 24px;
    box-shadow: var(--shadow);
  }
  .card--front { left: 168px; top: 200px; background: var(--card-light); color: var(--ink); }
  .card--back { left: 552px; top: 571px; background: var(--card-dark); color: var(--ink-inverse); }

  .contact-row {
    position: absolute; left: 0; width: 100%; height: 32px;
    display: flex; align-items: center;
  }
  .contact-row--top { top: 21px; }
  .contact-row--bottom { top: 220px; }

  .rule { height: 2px; background: var(--ink); flex: none; }
  .rule--lead { width: 31px; }
  .rule--tail { width: 30px; }
  .rule--tick { width: 11px; }
  .rule--fill { flex: 1 1 auto; }

  .contact-name {
    flex: none; margin: 0 6px;
    font-size: 20px; line-height: 24px; white-space: nowrap;
    position: relative; top: -1px;
  }
  .phone-icon { flex: none; width: 32px; height: 32px; display: block; }
  .contact-phone {
    flex: none; margin: 0 9px 0 10px;
    font-family: "Montserrat", "Arial", sans-serif;
    font-weight: 500; font-size: 12.5px; line-height: 14px; letter-spacing: 0.2px;
    white-space: nowrap;
  }

  .brand-name {
    position: absolute; left: 0; width: 100%; top: 122px;
    text-align: center;
    font-size: 25px; letter-spacing: 0.5px; line-height: 30px;
    white-space: nowrap;
  }
  .card--back .brand-name { color: var(--ink-inverse); }
</style>
</head>
<body>

<section class="card card--front" aria-label="Card front">
  <div class="contact-row contact-row--top">
    <span class="rule rule--lead"></span>
    <span class="contact-name">Nolan Pritchett</span>
    <span class="rule rule--tick"></span>
    <svg class="phone-icon" viewBox="0 0 32 32" aria-hidden="true">
      <circle cx="16" cy="16" r="15" fill="none" stroke="#111" stroke-width="2"/>
      <path d="M9 14.5c0-3 3.5-4.5 7-4.5s7 1.5 7 4.5v1h-3v-1.5h-8v1.5h-3z M11 16.5h10l2 5.5h-14z" fill="#111"/>
      <circle cx="16" cy="19.5" r="1.8" fill="#fff"/>
    </svg>
    <span class="rule rule--tick"></span>
    <span class="contact-phone">512-804-2271</span>
    <span class="rule rule--fill"></span>
  </div>

  <div class="brand-name">R &amp; T Summit Construction</div>

  <div class="contact-row contact-row--bottom">
    <span class="rule rule--fill"></span>
    <span class="contact-name">Curtis Hale</span>
    <span class="rule rule--tick"></span>
    <svg class="phone-icon" viewBox="0 0 32 32" aria-hidden="true">
      <circle cx="16" cy="16" r="15" fill="none" stroke="#111" stroke-width="2"/>
      <path d="M9 14.5c0-3 3.5-4.5 7-4.5s7 1.5 7 4.5v1h-3v-1.5h-8v1.5h-3z M11 16.5h10l2 5.5h-14z" fill="#111"/>
      <circle cx="16" cy="19.5" r="1.8" fill="#fff"/>
    </svg>
    <span class="rule rule--tick"></span>
    <span class="contact-phone">512-693-1804</span>
    <span class="rule rule--tail"></span>
  </div>
</section>

<section class="card card--back" aria-label="Card back">
  <div class="brand-name">R &amp; T Summit Construction</div>
</section>

</body>
</html>
```